new KVR one page flyer

We need a 1 page A4 size flyer (need it asap please) that describes on 1 page with art work and using photos the services we provide. I have included some examples of old previous flyers from our other (seperate divisions of the business) I have named a photo called (photo for top of design) however you do your design this photo needs to be the star of the page by either having it at the top or bottom of the page please and we usually like this photo to be in greyscale colour.
we do like greyscale designs but are open to see what you come up with as a whole page of grey white and black might not suit.

Needs to list the following

Services include:
Over size loads / Hot Shot Loads
Heavy Vehicle Recovery services
Potable Water Deliveries
Road Building / Maintenance
Earthworks
Sand & Metal Supply & Cartage
Road Train Tippers
Road Train Tankers
Road Train Flat Tops
Drop Deck Trailers
Mine site accredited equipment & Operators.

We offer a large rage of services not listed so call us today for a personalised quote to suit your needs.

To go on the bottom of the page our contact details are

KVR Pty Ltd
Depot: Lot 514, Banksia Flats Track Coober Pedy
Mobile: 047 216 9381
email: darren@kestrelvaleroadworks.com.au

Target Market(s)

new clients

Colors

Designer to choose colors to be used in the design.

Requirements
Must have
• our services listed
Nice to have
• stand out designs

```html
<!DOCTYPE html>
<html lang="en">
<head>
<meta charset="utf-8">
<title>KVR Services Flyer</title>
<link rel="stylesheet" href="https://fonts.googleapis.com/css2?family=Lato:wght@400;700;900&family=Oswald:wght@400;500&display=swap">
<style>
  :root {
    --ink: #0c0b0a;
    --panel-top: #221c18;
    --panel-bottom: #0d0c0b;
    --gold: #ad8748;
    --gold-deep: #8f6c36;
    --gold-text: #c49a55;
    --cream: #f3e2bf;
    --silver-light: #f2f2f2;
    --silver-mid: #a8a8a8;
    --silver-dark: #5b5b5b;
    --text: #f4f1ec;
  }
  * { box-sizing: border-box; margin: 0; padding: 0; }
  html, body { width: 1007px; height: 1200px; overflow: hidden; background: var(--ink); }
  .flyer {
    position: relative;
    width: 1007px;
    height: 1200px;
    overflow: hidden;
    background: radial-gradient(ellipse at 40% 55%, var(--panel-top) 0%, var(--panel-bottom) 75%);
    font-family: "Lato", sans-serif;
    color: var(--text);
  }
  .hero { position: absolute; left: 0; top: 0; width: 1007px; height: 800px; }
  .brand-name {
    position: absolute;
    left: 30px;
    top: 570px;
    font-family: "Lato", sans-serif;
    font-weight: 900;
    font-size: 128px;
    line-height: 1;
    letter-spacing: 6px;
    color: #c9c9c9;
  }
  .offer-text {
    position: absolute;
    left: 702px;
    top: 545px;
    width: 220px;
    text-align: center;
    font-size: 19px;
    line-height: 27px;
    color: var(--cream);
  }
  .services-title {
    position: absolute;
    left: 43px;
    top: 720px;
    font-family: "Oswald", sans-serif;
    font-weight: 500;
    font-size: 33px;
    letter-spacing: -0.5px;
    color: var(--gold-text);
    text-transform: uppercase;
  }
  .services-list {
    position: absolute;
    top: 778px;
    list-style: none;
  }
  .services-list.col-left { left: 36px; }
  .services-list.col-right { left: 496px; }
  .services-list li {
    display: flex;
    align-items: center;
    height: 32px;
    font-size: 21px;
    white-space: nowrap;
  }
  .bullet {
    width: 18px; height: 18px;
    margin-right: 16px;
    flex: none;
  }
  .gallery { position: absolute; top: 990px; left: 0; width: 1007px; height: 126px; }
  .gallery-photo {
    position: absolute;
    top: 0;
    width: 304px;
    height: 124px;
    border: 2px solid #e8e8e8;
    border-radius: 8px;
    box-shadow: 0 0 6px rgba(0,0,0,0.6);
    background: linear-gradient(180deg, #6e9ad6 0%, #b9d2ee 48%, #b56a42 56%, #9c5434 100%);
  }
  .gallery-photo.graders { left: 26px; transform: skewX(-1.5deg); }
  .gallery-photo.tankers { left: 347px; transform: skewX(-1.5deg); }
  .gallery-photo.float { left: 669px; transform: skewX(-1.5deg); }
  .contact-band {
    position: absolute;
    left: 0;
    top: 1142px;
    width: 724px;
    height: 49px;
    background: var(--gold);
    clip-path: polygon(0 0, 100% 0, 95.5% 100%, 0 100%);
    display: flex;
    align-items: center;
    padding-left: 22px;
    font-family: "Oswald", sans-serif;
    font-size: 18.5px;
    color: #ffffff;
    white-space: nowrap;
  }
  .contact-band .divider { margin: 0 8px; }
  .phone {
    position: absolute;
    left: 750px;
    top: 1142px;
    height: 49px;
    display: flex;
    align-items: center;
    font-family: "Oswald", sans-serif;
    font-size: 34px;
    color: #ffffff;
    letter-spacing: 1px;
  }
  .phone-icon { width: 30px; height: 30px; margin-right: 12px; }
</style>
</head>
<body>
<main class="flyer">
  <svg class="hero" viewBox="0 0 1007 800" xmlns="http://www.w3.org/2000/svg">
    <defs>
      <linearGradient id="heroPhotoTone" x1="0" y1="0" x2="0" y2="1">
        <stop offset="0" stop-color="#2c2f36"/>
        <stop offset="0.35" stop-color="#676c74"/>
        <stop offset="0.55" stop-color="#8c8f92"/>
        <stop offset="0.62" stop-color="#6b4a34"/>
        <stop offset="1" stop-color="#a56a45"/>
      </linearGradient>
      <linearGradient id="silverStripe" x1="0" y1="0" x2="1" y2="0.3">
        <stop offset="0" stop-color="var(--silver-dark)"/>
        <stop offset="0.3" stop-color="var(--silver-light)"/>
        <stop offset="0.6" stop-color="var(--silver-mid)"/>
        <stop offset="1" stop-color="var(--silver-light)"/>
      </linearGradient>
      <linearGradient id="goldStripe" x1="0" y1="0" x2="1" y2="0">
        <stop offset="0" stop-color="var(--gold-deep)"/>
        <stop offset="1" stop-color="var(--gold)"/>
      </linearGradient>
    </defs>
    <polygon role="img" aria-label="Greyscale photo of a road train with side tipper trailers on a red dirt outback yard under a cloudy sky"
             points="0,0 1007,0 1007,362 690,588 0,414" fill="url(#heroPhotoTone)"/>
    <polygon class="stripe-silver-left" points="0,414 690,588 712,606 0,458" fill="url(#silverStripe)"/>
    <polygon class="stripe-gold-left" points="290,484 700,596 690,614" fill="url(#goldStripe)"/>
    <polygon class="stripe-gold-right" points="690,588 1007,362 1007,382 712,606" fill="var(--gold)"/>
    <polygon class="stripe-silver-right" points="760,606 1007,430 1007,470 800,606" fill="url(#silverStripe)"/>
    <polygon class="offer-burst" transform="translate(812,625) scale(1.1)" fill="var(--gold)"
      points="120,0 102.4,18.1 112.8,41 90.1,52 91.9,77.2 66.9,79.7 60,103.9 35.6,97.7 20.8,118.2 0,104 -20.8,118.2 -35.6,97.7 -60,103.9 -66.9,79.7 -91.9,77.2 -90.1,52 -112.8,41 -102.4,18.1 -120,0 -102.4,-18.1 -112.8,-41 -90.1,-52 -91.9,-77.2 -66.9,-79.7 -60,-103.9 -35.6,-97.7 -20.8,-118.2 0,-104 20.8,-118.2 35.6,-97.7 60,-103.9 66.9,-79.7 91.9,-77.2 90.1,-52 112.8,-41 102.4,-18.1"/>
  </svg>

  <div class="brand-name">KVR</div>

  <p class="offer-text">We offer a large rage<br>of services not listed<br>so call us today<br>for a personalised<br>quote to suit your<br>needs.</p>

  <h2 class="services-title">Services Include:</h2>

  <ul class="services-list col-left">
    <li><svg class="bullet" viewBox="0 0 18 18"><circle cx="9" cy="9" r="7.5" fill="none" stroke="var(--gold)" stroke-width="1.6"/><path d="M7.5 5.5 L11 9 L7.5 12.5" fill="none" stroke="var(--gold)" stroke-width="1.8"/></svg>Over size loads / Hot Shot Loads</li>
    <li><svg class="bullet" viewBox="0 0 18 18"><circle cx="9" cy="9" r="7.5" fill="none" stroke="var(--gold)" stroke-width="1.6"/><path d="M7.5 5.5 L11 9 L7.5 12.5" fill="none" stroke="var(--gold)" stroke-width="1.8"/></svg>Heavy Vehicle Recovery services</li>
    <li><svg class="bullet" viewBox="0 0 18 18"><circle cx="9" cy="9" r="7.5" fill="none" stroke="var(--gold)" stroke-width="1.6"/><path d="M7.5 5.5 L11 9 L7.5 12.5" fill="none" stroke="var(--gold)" stroke-width="1.8"/></svg>Potable Water Deliveries</li>
    <li><svg class="bullet" viewBox="0 0 18 18"><circle cx="9" cy="9" r="7.5" fill="none" stroke="var(--gold)" stroke-width="1.6"/><path d="M7.5 5.5 L11 9 L7.5 12.5" fill="none" stroke="var(--gold)" stroke-width="1.8"/></svg>Road Building / Maintenance</li>
    <li><svg class="bullet" viewBox="0 0 18 18"><circle cx="9" cy="9" r="7.5" fill="none" stroke="var(--gold)" stroke-width="1.6"/><path d="M7.5 5.5 L11 9 L7.5 12.5" fill="none" stroke="var(--gold)" stroke-width="1.8"/></svg>Earthworks</li>
    <li><svg class="bullet" viewBox="0 0 18 18"><circle cx="9" cy="9" r="7.5" fill="none" stroke="var(--gold)" stroke-width="1.6"/><path d="M7.5 5.5 L11 9 L7.5 12.5" fill="none" stroke="var(--gold)" stroke-width="1.8"/></svg>Sand &amp; Metal Supply &amp; Cartage</li>
  </ul>

  <ul class="services-list col-right">
    <li><svg class="bullet" viewBox="0 0 18 18"><circle cx="9" cy="9" r="7.5" fill="none" stroke="var(--gold)" stroke-width="1.6"/><path d="M7.5 5.5 L11 9 L7.5 12.5" fill="none" stroke="var(--gold)" stroke-width="1.8"/></svg>Road Train Tippers</li>
    <li><svg class="bullet" viewBox="0 0 18 18"><circle cx="9" cy="9" r="7.5" fill="none" stroke="var(--gold)" stroke-width="1.6"/><path d="M7.5 5.5 L11 9 L7.5 12.5" fill="none" stroke="var(--gold)" stroke-width="1.8"/></svg>Road Train Tankers</li>
    <li><svg class="bullet" viewBox="0 0 18 18"><circle cx="9" cy="9" r="7.5" fill="none" stroke="var(--gold)" stroke-width="1.6"/><path d="M7.5 5.5 L11 9 L7.5 12.5" fill="none" stroke="var(--gold)" stroke-width="1.8"/></svg>Road Train Flat Tops</li>
    <li><svg class="bullet" viewBox="0 0 18 18"><circle cx="9" cy="9" r="7.5" fill="none" stroke="var(--gold)" stroke-width="1.6"/><path d="M7.5 5.5 L11 9 L7.5 12.5" fill="none" stroke="var(--gold)" stroke-width="1.8"/></svg>Drop Deck Trailers</li>
    <li><svg class="bullet" viewBox="0 0 18 18"><circle cx="9" cy="9" r="7.5" fill="none" stroke="var(--gold)" stroke-width="1.6"/><path d="M7.5 5.5 L11 9 L7.5 12.5" fill="none" stroke="var(--gold)" stroke-width="1.8"/></svg>Mine site accredited equipment &amp; Operators</li>
    <li><svg class="bullet" viewBox="0 0 18 18"><circle cx="9" cy="9" r="7.5" fill="none" stroke="var(--gold)" stroke-width="1.6"/><path d="M7.5 5.5 L11 9 L7.5 12.5" fill="none" stroke="var(--gold)" stroke-width="1.8"/></svg>And many more</li>
  </ul>

  <section class="gallery">
    <div class="gallery-photo graders" role="img" aria-label="Photo of road graders and a loader working on a red dirt site under blue sky"></div>
    <div class="gallery-photo tankers" role="img" aria-label="Photo of road train prime movers parked beside a dome shelter"></div>
    <div class="gallery-photo float" role="img" aria-label="Photo of a prime mover hauling a grader on a drop deck trailer"></div>
  </section>

  <footer>
    <div class="contact-band">Lot 514, Banksia Flats Track Coober Pedy<span class="divider">|</span>darren@kestrelvaleroadworks.com.au</div>
    <div class="phone">
      <svg class="phone-icon" viewBox="0 0 30 30">
        <circle cx="15" cy="15" r="13" fill="none" stroke="#ffffff" stroke-width="2"/>
        <path d="M10.5 8.5 L13 8 L14.3 11.5 L12.6 12.8 C13.4 14.7 15.2 16.6 17.2 17.4 L18.5 15.7 L22 17 L21.5 19.5 C21.2 20.6 20 21.3 18.8 21 C13.8 19.8 10.2 16.2 9 11.2 C8.7 10 9.4 8.8 10.5 8.5 Z" fill="#ffffff"/>
      </svg>
      047 216 9381
    </div>
  </footer>
</main>
</body>
</html>
```